Web Design for an Online Dating Web Site

We need an uncoded web design for a new online dating web site called zMatchy.net. Simplicity and boldness are the key factors in the successful design.
Please look at the requirements document attached for details.
Updates
Dear all,
Please AVOID USING A PICTURE OF A HAPPY COUPLE ON THE HOME PAGE of the site. We highly want to move away from this space as it makes our web site just like another dating web site.
We like something simple with web 2.0 look and feel. The examples in the Requirements Document are exactly the design we are after.
Regards
Tarn
Industry/Entity Type
Dating
Look and feel
Each slider illustrates characteristics of the customer's brand and the style your logo design should communicate.

```html
<!DOCTYPE html>
<html lang="en">
<head>
<meta charset="utf-8">
<title>zMatchy.net</title>
<link rel="stylesheet" href="https://fonts.googleapis.com/css2?family=Arimo:wght@400;700&family=PT+Sans:ital,wght@0,700;1,400&display=swap">
<style>
:root{
  --pink:#e9458f;
  --pink-dark:#d9337d;
  --grey:#7a7a7e;
  --grey-dark:#58585c;
  --text:#555558;
  --bg:#e6e6e6;
  --hero:#ecd2dc;
  --panel:#d8d8d8;
  --field:#141414;
}
*{box-sizing:border-box;margin:0;padding:0}
html,body{width:1200px;height:1134px;overflow:hidden}
body{background:var(--bg);font-family:Arimo,Arial,sans-serif;color:var(--text);position:relative}
.abs{position:absolute}
a{color:inherit;text-decoration:none}

.brand{left:197px;top:16px;font-size:64px;font-weight:700;color:var(--pink);line-height:1;letter-spacing:-2px;display:flex;align-items:center;gap:10px}
.brand .dot{width:20px;height:20px;background:var(--grey);border-radius:50%}
.brand-url{left:400px;top:94px;font-size:15px;line-height:1;color:var(--grey)}

.social-top{left:849px;top:15px;display:flex;gap:8px}
.social-top span{width:26px;height:26px;background:var(--grey);border-radius:3px}

.nav{left:741px;top:51px;display:flex;gap:4px}
.nav a{height:30px;line-height:30px;padding:0 8px;background:var(--grey);color:#fff;font-size:12.5px;border-radius:2px}
.nav a.active{background:var(--pink)}

.login{left:739px;top:87px;width:272px;height:72px;background:var(--panel);border-radius:3px}
.login label{position:absolute;left:6px;font-size:11px;color:#333}
.login .field{position:absolute;left:63px;width:102px;height:20px;background:#d0d0d0;border:1px solid #c2c2c2}
.login .btn{position:absolute;left:172px;top:19px;width:51px;height:31px;background:var(--pink);color:#fff;font-weight:700;font-size:12.5px;line-height:31px;text-align:center;border-radius:3px}

.welcome{left:198px;top:170px;width:814px;height:30px;display:flex;align-items:center;gap:6px}
.welcome::before,.welcome::after{content:"";flex:1;border-top:1px dashed #8a8a8a}
.welcome h2{color:var(--pink);font-size:27px;font-weight:700}

.hero{left:197px;top:216px;width:814px;height:251px;background:var(--hero)}
.hero h1{position:absolute;left:34px;top:20px;font-family:"PT Sans",sans-serif;font-size:34px;font-weight:700;color:#5a4d55;white-space:nowrap}
.hero h1 em{font-style:normal;color:var(--pink)}
.hero .sub{position:absolute;left:34px;top:56px;font-family:"PT Sans",sans-serif;font-style:italic;font-size:26px;color:#5a4d55}
.hero .body{position:absolute;left:34px;top:94px;width:530px;font-size:10.5px;line-height:15.5px;color:#555}
.hero .cta{position:absolute;left:33px;top:158px;width:180px;height:65px;background:linear-gradient(#f06aa6,var(--pink-dark));color:#fff;font-size:32px;font-weight:700;line-height:65px;text-align:center;border-radius:2px}
.hero .dots{position:absolute;left:240px;top:212px;display:flex;gap:6px}
.hero .dots span{width:12px;height:12px;border-radius:50%;background:#8a7d84}
.hero .dots span.on{background:#e6157f}
.hero svg.arrow{position:absolute;top:94px}

.about-h{left:207px;top:499px;font-size:25px;font-weight:700;color:var(--grey-dark)}
.about-p{left:205px;top:535px;width:555px;font-size:10.5px;line-height:15.5px}
.member{width:76px}
.member .photo{width:76px;height:87px;border:1px solid #fff}
.member b{display:block;margin-top:6px;color:var(--pink);font-size:11px;text-align:center}
.member small{display:block;font-size:11px;padding-left:8px}

.posts-h{left:812px;top:499px;width:200px;text-align:center;font-size:25px;font-weight:700;color:var(--grey-dark)}
.post{left:812px;font-size:13px;line-height:17px}
.post .t{color:var(--grey)}
.post .m{color:var(--pink)}
.post .m b{color:var(--grey-dark)}

.divider{left:202px;top:771px;width:810px;border-top:1px dashed #8a8a8a}

.foot-brand{left:197px;top:787px;font-size:38px;font-weight:700;color:var(--pink);display:flex;align-items:center;gap:6px;line-height:1}
.foot-brand .dot{width:12px;height:12px;background:var(--grey);border-radius:50%}
.contact{left:198px;top:840px;font-size:11px;line-height:17px;color:var(--grey)}
.contact u{display:block}
.links{left:420px;top:840px;font-size:11px;line-height:34px;color:var(--grey);list-style:none}

.talk-h{left:608px;top:782px;font-size:26px;color:var(--pink)}
.talk-s{left:610px;top:815px;font-size:12.5px;color:#333;letter-spacing:.5px}
.in{left:611px;background:var(--field);color:#ddd;font-size:11px;padding:6px 12px;border-radius:2px}
.send{left:610px;top:1033px;width:120px;height:31px;background:var(--pink);color:#fff;font-size:10px;font-weight:700;line-height:31px;text-align:center;border-radius:3px;letter-spacing:.3px}

.follow{left:840px;width:171px;display:flex;align-items:center;justify-content:flex-end;gap:6px;font-size:10.5px;color:var(--grey)}
.follow span{width:26px;height:26px;border-radius:3px;background:var(--grey)}

.bottom{top:1092px;font-size:10.5px;color:#444;letter-spacing:.3px}
</style>
</head>
<body>

<div class="abs brand">zMatchy<span class="dot"></span></div>
<div class="abs brand-url">zmatchy.net</div>

<div class="abs social-top"><span></span><span></span><span></span><span></span><span></span></div>

<nav class="abs nav">
  <a class="active" href="#">Why</a><a href="#">How It Works</a><a href="#">Sign Up</a><a href="#">Our Blog</a>
</nav>

<form class="abs login">
  <label style="top:17px">Username</label><span class="field" style="top:13px"></span>
  <label style="top:44px;left:9px">Password</label><span class="field" style="top:40px"></span>
  <span class="btn">Login</span>
</form>

<div class="abs welcome"><h2>- WELCOME -</h2></div>

<section class="abs hero">
  <h1><em>Lorem ipsum dolor sit amet,</em> consectetur adipiscing,</h1>
  <p class="sub">Lorem ipsum dolor sit amet, consectetur adipiscing elit.</p>
  <p class="body">Lorem ipsum dolor sit amet, consectetur adipiscing elit. Integer dictum, neque ut imperdiet pellentesque, nulla tellus tempus. Pellentesque tincidunt fermentum diam sagittis ullamcorper. Lorem ipsum dolor sit amet, consectetur adipiscing elit. Integer dictum.</p>
  <a class="cta" href="#">SIGN UP</a>
  <div class="dots"><span class="on"></span><span></span><span></span><span></span><span></span></div>
  <svg class="arrow" style="left:9px" width="14" height="42" viewBox="0 0 14 42"><path d="M12 1 L2 21 L12 41" fill="none" stroke="#666" stroke-width="1.2"/></svg>
  <svg class="arrow" style="left:793px" width="14" height="42" viewBox="0 0 14 42"><path d="M2 1 L12 21 L2 41" fill="none" stroke="#666" stroke-width="1.2"/></svg>
</section>

<h2 class="abs about-h">About Us</h2>
<p class="abs about-p">Lorem ipsum dolor sit amet, consectetur adipiscing elit. Integer dictum, neque ut imperdiet pellentesque, nulla tellus tempus. Pellentesque tincidunt fermentum diam sagittis ullamcorper. Lorem ipsum dolor sit amet, consectetur diam sagittis ullamcorper. Lorem ipsum dolor sit amet, consectetur adipiscing elit. Integer dictum. Lorem ipsum dolor sit amet, consectetur adipiscing elit. Integer dictum.</p>

<div class="abs member" style="left:204px;top:619px"><div class="photo" role="img" aria-label="Member photo: couple on a beach" style="background:linear-gradient(160deg,#7ea3b4,#c98f84 60%,#e3c3c8)"></div><b>Lorem ipsum</b><small>sit amet,</small></div>
<div class="abs member" style="left:322px;top:619px"><div class="photo" role="img" aria-label="Member photo: smiling couple" style="background:linear-gradient(160deg,#3a2418,#b07a58 55%,#6cbf3a)"></div><b>Lorem ipsum</b><small>sit amet,</small></div>
<div class="abs member" style="left:440px;top:619px"><div class="photo" role="img" aria-label="Member photo: couple embracing" style="background:linear-gradient(160deg,#e9e9e9,#b79a88 50%,#2a2a2e)"></div><b>Lorem ipsum</b><small>sit amet,</small></div>
<div class="abs member" style="left:559px;top:619px"><div class="photo" role="img" aria-label="Member photo: couple by the sea" style="background:linear-gradient(160deg,#9fd2ef,#e2c0a0 55%,#f2f2f2)"></div><b>Lorem ipsum</b><small>sit amet,</small></div>

<h2 class="abs posts-h">- Recent Posts -</h2>
<div class="abs post" style="top:534px"><div class="t">Online dating</div><div class="m">Jul 27, 2011 | 2 Comments | <b>read</b></div></div>
<div class="abs post" style="top:593px"><div class="t">Online dating</div><div class="m">Jul 27, 2011 | 2 Comments | <b>read</b></div></div>
<div class="abs post" style="top:648px"><div class="t">Online dating</div><div class="m">Jul 27, 2011 | 2 Comments | <b>read</b></div></div>
<div class="abs post" style="top:709px"><div class="t">Online dating</div><div class="m">Jul 27, 2011 | 2 Comments | <b>read</b></div></div>

<div class="abs divider"></div>

<div class="abs foot-brand">zMatchy<span class="dot"></span></div>
<div class="abs contact">
  Call Us<br>150200 7 386<br><br><u>Email Us</u><br>Address<br>2280 Larkmoor Ave.<br>Brindle Bay, CAxcs
</div>
<ul class="abs links">
  <li>+ Why zMatchy</li><li>+ How it works</li><li>+ Sign Up</li><li>+ Login</li><li>+ About Us</li>
</ul>

<h2 class="abs talk-h" style="font-weight:400">Let's Talk</h2>
<p class="abs talk-s">drop us a message</p>
<div class="abs in" style="top:842px;width:161px;height:24px">Name</div>
<div class="abs in" style="top:876px;width:161px;height:24px">Email</div>
<div class="abs in" style="top:910px;width:221px;height:119px">Comments</div>
<a class="abs send" href="#">SEND YOUR MESSAGE</a>

<div class="abs follow" style="top:850px">Become a fan <span></span></div>
<div class="abs follow" style="top:884px">Follow us on Chirper <span></span></div>
<div class="abs follow" style="top:919px">us on Stumble Deck <span></span></div>
<div class="abs follow" style="top:953px">Subscribe us Circle+ <span></span></div>

<div class="abs bottom" style="left:198px">© 2011 zMatchy.net</div>
<div class="abs bottom" style="left:824px">Privacy Policy</div>
<div class="abs bottom" style="left:917px">Terms &amp; Conditions</div>

</body>
</html>
```